Stationary and Business Card
Medical Practice
I need single sided standard sized Business Card [3.5" x 2"]
Letter type / font / color is up to the designer.
Professional
Benedict Harwell, MD
Torrance Ridge-Velmont Building
Suite 460
4127 Almaden Avenue
La Jolla, CA 92037
contact@brinmoor-example.com
www.drharwell-example.com
Please use provided logo.
Please visit drharwell-example.com for any additional creative direction.
Do not include email address.
Please provide a version with www.drharwell-example.com on the back of the card and a version with the web address on the front.

```html
<!DOCTYPE html>
<html lang="en">
<head>
<meta charset="utf-8">
<title>Harwell Facial Plastic Surgery – Business Cards</title>
<link rel="stylesheet" href="https://fonts.googleapis.com/css2?family=Cinzel:wght@400;600;700&display=swap">
<style>
  :root {
    --stage: #8d8f92;
    --stage-dark: #5f6164;
    --navy: #12154a;
    --royal: #2b3bd6;
    --ink: #1c2a78;
    --purple: #3a2c98;
    --purple-deep: #2a1f7a;
    --paper: #ffffff;
    --paper-grey: #e7e8ea;
    --text-dark: #2b2b3a;
  }
  * { box-sizing: border-box; margin: 0; padding: 0; }
  html, body { width: 1200px; height: 374px; overflow: hidden; }
  body {
    background: radial-gradient(ellipse at 50% 45%, var(--stage) 0%, var(--stage-dark) 100%);
    font-family: "Cinzel", serif;
    position: relative;
  }
  .card {
    position: absolute;
    top: 79px;
    width: 362px;
    height: 215px;
    border-radius: 12px;
    overflow: hidden;
    box-shadow: 0 4px 10px rgba(0,0,0,.35);
  }
  .card--front { left: 28px; background: var(--paper); }
  .card--back-light { left: 420px; background: linear-gradient(180deg, #fafafa 0%, var(--paper-grey) 100%); }
  .card--back-dark { left: 812px; background: linear-gradient(180deg, var(--purple) 0%, var(--purple-deep) 100%); }

  .chevron { position: absolute; right: 0; top: 0; width: 362px; height: 215px; }

  .brand { display: flex; align-items: center; gap: 7px; }
  .brand__mark { width: 24px; height: 24px; background: var(--royal); flex: none; }
  .brand__name { font-size: 26px; font-weight: 600; letter-spacing: 1px; color: var(--ink); line-height: 1; }
  .brand__tag { font-size: 8.5px; font-weight: 700; color: var(--royal); letter-spacing: .5px; margin-top: 3px; }

  .card--front .brand-block { position: absolute; left: 18px; top: 20px; }
  .card--front .brand__name { font-size: 24px; }

  .contact { position: absolute; left: 18px; top: 98px; color: var(--text-dark); }
  .contact__name { font-size: 11px; font-weight: 600; color: var(--ink); margin-bottom: 6px; }
  .contact__line { font-size: 6.6px; line-height: 9.5px; letter-spacing: .2px; }
  .card--front .web { position: absolute; left: 18px; bottom: 16px; font-size: 7px; color: var(--text-dark); }

  .centered { position: absolute; left: 0; right: 0; top: 78px; display: flex; justify-content: center; }
  .web--center { position: absolute; left: 0; right: 0; bottom: 14px; text-align: center; font-size: 10px; font-weight: 600; letter-spacing: .4px; }
  .card--back-light .web--center { color: var(--ink); }
  .card--back-dark .web--center { color: var(--paper); }
  .card--back-dark .brand__mark { background: var(--paper); }
  .card--back-dark .brand__name, .card--back-dark .brand__tag { color: var(--paper); }
</style>
</head>
<body>

<section class="card card--front">
  <svg class="chevron" viewBox="0 0 362 215" aria-hidden="true">
    <defs>
      <linearGradient id="band" x1="0" x2="1" y1="0" y2="0">
        <stop offset="0" stop-color="#3d52ff"/>
        <stop offset="1" stop-color="#1a2399"/>
      </linearGradient>
    </defs>
    <polygon points="292,0 362,0 362,215 292,215 238,107.5" fill="url(#band)"/>
    <polygon points="312,0 362,0 362,215 312,215 262,107.5" fill="#0b0d2e"/>
    <polygon points="330,0 362,0 362,215 330,215 284,107.5" fill="var(--navy)"/>
  </svg>
  <div class="brand-block">
    <div class="brand">
      <span class="brand__mark"></span>
      <span class="brand__name">HARWELL</span>
    </div>
    <p class="brand__tag">FACIAL PLASTIC SURGERY</p>
  </div>
  <div class="contact">
    <p class="contact__name">Benedict Harwell, MD</p>
    <p class="contact__line">Torrance Ridge-Velmont Building</p>
    <p class="contact__line">Suite 460</p>
    <p class="contact__line">4127 Almaden Avenue</p>
    <p class="contact__line">La Jolla, CA 92037</p>
    <p class="contact__line">P 858.555.0142 | F 858.555.0187</p>
  </div>
  <p class="web">www.drharwell-example.com</p>
</section>

<section class="card card--back-light">
  <div class="centered">
    <div>
      <div class="brand">
        <span class="brand__mark"></span>
        <span class="brand__name">HARWELL</span>
      </div>
      <p class="brand__tag">FACIAL PLASTIC SURGERY</p>
    </div>
  </div>
  <p class="web--center">WWW.DRHARWELL-EXAMPLE.COM</p>
</section>

<section class="card card--back-dark">
  <div class="centered">
    <div>
      <div class="brand">
        <span class="brand__mark"></span>
        <span class="brand__name">HARWELL</span>
      </div>
      <p class="brand__tag">FACIAL PLASTIC SURGERY</p>
    </div>
  </div>
  <p class="web--center">WWW.DRHARWELL-EXAMPLE.COM</p>
</section>

</body>
</html>
```